A comunicação apenas pelo chat ou com desenvolvedor que não se comunica com cliente é péssimo ! O desenvolvedor que não se comunica dificulta o desenvolvimento do trabalho causando uma demora ecessiva !

```html
<!DOCTYPE html>
<html lang="pt-BR">
<head>
<meta charset="UTF-8">
<title>Cartão de Visita — Traço Firme Projetos</title>
<link href="https://fonts.googleapis.com/css2?family=Montserrat:wght@400;500;600&display=swap" rel="stylesheet">
<style>
  :root {
    --backdrop: #b5b5b5;
    --card-front: #ffffff;
    --card-back: #000000;
    --ink-light: #ffffff;
    --ink-soft: #d9d9d9;
    --shade: #262626;
  }
  * { margin: 0; padding: 0; box-sizing: border-box; }
  html, body {
    width: 1200px;
    height: 1200px;
    overflow: hidden;
    background: var(--backdrop);
    font-family: "Montserrat", Arial, sans-serif;
  }
  .canvas { position: relative; width: 1200px; height: 1200px; }

  .card { position: absolute; left: 207px; width: 786px; height: 456px; }
  .card-front { top: 94px; background: var(--card-front); }
  .card-back { top: 660px; background: var(--card-back); overflow: hidden; }

  .backdrop-block {
    position: absolute;
    left: 0; top: 168px;
    width: 574px; height: 288px;
    background: var(--shade);
  }

  .holder { position: absolute; right: 50px; top: 100px; text-align: right; color: var(--ink-light); }
  .holder-name { font-size: 30px; font-weight: 500; line-height: 1; }
  .holder-role { font-size: 19px; color: var(--ink-soft); margin-top: 6px; }

  .brand {
    position: absolute; left: 58px; top: 192px;
    display: flex; align-items: center; gap: 16px;
    color: var(--ink-light);
  }
  .brand-square { width: 58px; height: 58px; background: var(--ink-light); }
  .brand-name {
    font-size: 24px; font-weight: 400; letter-spacing: 3px;
    line-height: 1.2; text-transform: uppercase;
  }

  .contacts {
    position: absolute; right: 42px; top: 196px;
    list-style: none; color: var(--ink-light);
    font-size: 17px;
  }
  .contacts li {
    display: flex; justify-content: flex-end; align-items: center;
    gap: 10px; height: 28px;
  }
  .contacts li.gap { margin-top: 16px; }
  .contacts svg { width: 20px; height: 20px; flex: none; }
</style>
</head>
<body>
<main class="canvas">
  <section class="card card-front" aria-label="Frente do cartão"></section>

  <section class="card card-back" aria-label="Verso do cartão">
    <div class="backdrop-block"></div>

    <div class="holder">
      <p class="holder-name">Nome Sobrenome</p>
      <p class="holder-role">cargo</p>
    </div>

    <div class="brand">
      <span class="brand-square"></span>
      <span class="brand-name">Traço Firme<br>Projetos</span>
    </div>

    <ul class="contacts">
      <li>+55 37 8888-9999
        <svg viewBox="0 0 20 20" fill="none" stroke="#fff" stroke-width="1.8"><path d="M5 2.5l3 3.5-2 2c1 2.5 3 4.5 5.5 5.5l2-2 3.5 3-2 2.5C8.5 16.5 3.5 11.5 2.5 5z" stroke-linejoin="round"/></svg>
      </li>
      <li>contato@contato.com.br
        <svg viewBox="0 0 20 20" fill="none" stroke="#fff" stroke-width="1.8"><rect x="2" y="4.5" width="16" height="11"/><path d="M2 4.5l8 6 8-6"/></svg>
      </li>
      <li>www.site.com.br
        <svg viewBox="0 0 20 20" fill="none" stroke="#fff" stroke-width="1.6"><circle cx="10" cy="10" r="8"/><path d="M2 10h16M10 2c3 3 3 13 0 16M10 2c-3 3-3 13 0 16"/></svg>
      </li>
      <li class="gap">Endereço: Exemplo - N II
        <svg viewBox="0 0 20 20" fill="none" stroke="#fff" stroke-width="2"><circle cx="10" cy="10" r="6.5"/></svg>
      </li>
      <li>perfil/id
        <svg viewBox="0 0 20 20"><rect x="2" y="2" width="16" height="16" rx="2" fill="#fff"/></svg>
      </li>
    </ul>
  </section>
</main>
</body>
</html>
```